Tri-fold brochue, business card, and stationary design.

Tri-fold brochure: We are looking to get a tri-fold brochure template created so we can add our content on each side of the brochure and then leave these with prospective clients during sales calls.Business card: We would like the business card to have employee name, phone number, and email address on the card. We are open to rounded corners as well.We just redid our website and we'd like all designs to be complementary to our new "Look and feel" of our website.

Contact Information for Business Card

We would like the business card to have employee name, phone number, and email address on the card. We are open to rounded corners as well.

We just redid our website and we'd like all designs to be complementary to our new "Look and feel" of our website.

```html
<!DOCTYPE html>
<html lang="en">
<head>
<meta charset="utf-8">
<title>Harborline Networks – Business Card</title>
<link rel="stylesheet" href="https://fonts.googleapis.com/css2?family=Exo+2:wght@700&family=Raleway:wght@400;700&display=swap">
<style>
  :root {
    --page-bg: #c9c8cd;
    --card-white: #ffffff;
    --card-tint: #f3f3f5;
    --brand-blue: #1f97d4;
    --brand-blue-light: #35a9dd;
    --panel-dark: #222222;
    --accent-green: #a9cf4a;
    --accent-green-dark: #86a43c;
    --text-light: #ffffff;
  }
  * { margin: 0; padding: 0; box-sizing: border-box; }
  html, body { width: 1071px; height: 1200px; overflow: hidden; }
  body { background: var(--page-bg); position: relative; font-family: "Raleway", sans-serif; }

  .card {
    position: absolute;
    left: 198px;
    width: 674px;
    height: 436px;
    background: linear-gradient(135deg, var(--card-white) 0%, var(--card-tint) 45%, var(--card-white) 100%);
    overflow: hidden;
  }
  .card--front { top: 122px; }
  .card--back { top: 628px; }

  .brand-dot {
    position: absolute;
    border-radius: 50%;
    background: var(--brand-blue);
  }
  .brand-name {
    position: absolute;
    font-family: "Exo 2", sans-serif;
    font-weight: 700;
    color: var(--brand-blue);
    line-height: 1;
  }
  .brand-name .brand-sub { display: block; }

  .card--front .brand-dot { left: 154px; top: 158px; width: 92px; height: 92px; }
  .card--front .brand-name { left: 294px; top: 190px; font-size: 48px; }
  .card--front .brand-sub { font-size: 21px; letter-spacing: 16px; margin-top: 2px; }

  .card--back .brand-dot { left: 89px; top: 160px; width: 72px; height: 72px; }
  .card--back .brand-name { left: 0; width: 250px; top: 254px; font-size: 35px; text-align: center; }
  .card--back .brand-sub { font-size: 15px; letter-spacing: 11px; margin-top: 1px; padding-left: 11px; }

  .back-shapes { position: absolute; inset: 0; }

  .contact { position: absolute; color: var(--text-light); white-space: nowrap; }
  .contact--name { left: 360px; top: 113px; font-weight: 700; font-size: 24px; color: var(--accent-green); }
  .contact--title { left: 361px; top: 146px; font-size: 18px; }
  .contact--phone { left: 352px; top: 207px; font-size: 17px; }
  .contact--email { left: 345px; top: 247px; font-size: 18px; }
  .contact--web { left: 341px; top: 292px; font-size: 18px; }
</style>
</head>
<body>

<section class="card card--front">
  <span class="brand-dot"></span>
  <p class="brand-name">Harborline<span class="brand-sub">Networks</span></p>
</section>

<section class="card card--back">
  <svg class="back-shapes" width="674" height="436" viewBox="0 0 674 436">
    <defs>
      <clipPath id="tab-clip">
        <path d="M279 78 H318 Q340 78 338 100 L313 360 Q311 382 289 382 H243 Z"/>
      </clipPath>
    </defs>
    <polygon points="288,0 674,0 674,436 236,436" fill="var(--panel-dark)"/>
    <path d="M279 78 H318 Q340 78 338 100 L313 360 Q311 382 289 382 H243 Z" fill="var(--accent-green)"/>
    <g clip-path="url(#tab-clip)">
      <rect x="230" y="194" width="100" height="132" fill="var(--accent-green-dark)"/>
      <line x1="230" y1="238" x2="330" y2="238" stroke="var(--accent-green)" stroke-width="1.5"/>
      <line x1="230" y1="282" x2="330" y2="282" stroke="var(--accent-green)" stroke-width="1.5"/>
    </g>
    <!-- person icon -->
    <g fill="#fff">
      <circle cx="303" cy="128" r="7"/>
      <path d="M289 150 Q289 137 303 137 Q317 137 317 150 Z"/>
    </g>
    <!-- phone icon -->
    <path d="M286 211 l4 -2 l3 5 l-3 2 q2 5 6 8 l2 -3 l5 3 l-2 4 q-4 2 -10 -4 q-7 -7 -5 -13 z" fill="#fff"/>
    <!-- mail icon -->
    <g>
      <rect x="283" y="253" width="17" height="12" fill="#fff"/>
      <path d="M283 253 L291.5 260 L300 253" fill="none" stroke="var(--accent-green-dark)" stroke-width="1.3"/>
    </g>
    <!-- globe icon -->
    <g fill="none" stroke="#fff" stroke-width="1.5">
      <circle cx="291" cy="304" r="9"/>
      <ellipse cx="291" cy="304" rx="4" ry="9"/>
      <line x1="282" y1="304" x2="300" y2="304"/>
      <line x1="284" y1="299" x2="298" y2="299"/>
      <line x1="284" y1="309" x2="298" y2="309"/>
    </g>
  </svg>

  <span class="brand-dot"></span>
  <p class="brand-name">Harborline<span class="brand-sub">Networks</span></p>

  <p class="contact contact--name">Employee Name</p>
  <p class="contact contact--title">job title</p>
  <p class="contact contact--phone">555-013-4827</p>
  <p class="contact contact--email">sales@harborlinenet.com</p>
  <p class="contact contact--web">www.harborlinenet.com</p>
</section>

</body>
</html>
```